2019 Chase the Morning Comet (Cardio Calendar)

I would like to put together a calendar of cardio workouts for the year. I would have 4 different workouts per week + 2 basic steady state workouts. I envision a picture of me on the top page and along with the challenge of the month description and the 3 different types of cardio description. on the bottom page would be the calendar for that month with the workout typed into the box. I am not sure if a boxed calendar would be enough space to write each workout in so I am open to more ideas on how to present the workouts

Target Market(s)

Women 20-60 years old
moms
couples
men
athletes

Industry/Entity Type

Fitness

Font styles to use
Sans Serif

Colors

Designer to choose colors to be used in the design.

Requirements
Must have
• Ability to incorporate 4 different workouts per week in a downloadable calendar style
• I want to have a different picture available for each month
• modern, bold, but simple and clean presentation
Nice to have
• picture at the top, with a description of the 3 different types of workouts for that month.
• On the bottom would be space for separate days of each workout
Should not have
• NA

```html
<!DOCTYPE html>
<html lang="en">
<head>
<meta charset="utf-8">
<title>Chase the Morning Comet — January Cardio Calendar</title>
<link href="https://fonts.googleapis.com/css2?family=Montserrat:wght@400;500;600;700;800&display=swap" rel="stylesheet">
<style>
:root{
  --red:#d9163f;
  --dark:#0c1216;
  --band:#555758;
  --band-light:#6c6d6e;
  --cell:#dedede;
  --column:#6d6d6d;
  --white:#ffffff;
  --ink:#444;
}
*{margin:0;padding:0;box-sizing:border-box}
html,body{width:776px;height:1200px;overflow:hidden;background:#fff}
body{font-family:'Montserrat',sans-serif;position:relative}
.page{position:relative;width:776px;height:1200px;overflow:hidden;background:#fff}
.hero{position:absolute;left:0;top:0;width:776px;height:541px;
  background:
   radial-gradient(ellipse 60% 40% at 55% 55%, rgba(120,120,130,.25), transparent 70%),
   linear-gradient(180deg,#070b10 0%,#0d1a22 35%,#15251c 60%,#2d5a22 82%,#3e6f2a 100%)}
.challenge{position:absolute;left:34px;top:46px;color:var(--white);font-weight:700;font-size:26px;line-height:36px;font-variant:small-caps;letter-spacing:.5px}
.divider{position:absolute;left:175px;top:50px;width:2px;height:130px;background:var(--white)}
.intro{position:absolute;left:196px;top:50px;width:226px;color:#d8d8d8;font-size:8.6px;line-height:11.7px}
.month{position:absolute;left:33px;top:488px;width:180px;height:53px;border-left:3px solid var(--white);border-top:3px solid var(--white)}
.month span{position:absolute;left:20px;top:6px;color:var(--white);font-weight:700;font-size:36px;letter-spacing:.5px}
.types{position:absolute;left:606px;top:51px;width:151px;height:150px;background:var(--red);border-radius:8px 8px 0 0;color:var(--white);text-align:center}
.types .num{font-size:84px;font-weight:600;line-height:1;margin-top:16px}
.types .label{font-size:16px;font-weight:700;font-variant:small-caps;margin-top:10px}
.sidebar{position:absolute;left:606px;top:201px;width:151px;height:340px;background:rgba(60,60,60,.72);padding:0 10px}
.column{position:absolute;left:606px;top:541px;width:151px;height:659px;background:var(--column)}
.cardio{position:absolute;left:10px;width:135px;color:var(--white)}
.cardio h3{font-size:16px;font-weight:700;font-variant:small-caps;display:inline-block;border-bottom:1px solid var(--white);padding-bottom:2px;margin-bottom:6px}
.cardio p{font-size:6.6px;font-weight:700;line-height:9.3px}
.note-line{position:absolute;left:22px;width:107px;height:2px;background:var(--white)}
.week{position:absolute;left:35px;width:534px;height:90px}
.week .tag{position:absolute;left:0;top:0;width:90px;height:90px;background:var(--red);border-radius:10px 0 0 10px;color:var(--white);text-align:center}
.tag .n{font-size:38px;font-weight:600;line-height:1;margin-top:14px;letter-spacing:1px}
.tag .w{font-size:17px;font-weight:500;margin-top:3px}
.grid{position:absolute;left:94px;top:0;width:440px;font-size:8.5px;font-weight:700;color:var(--white)}
.row{display:flex;gap:2px;margin-bottom:3px}
.row div{display:flex;align-items:center;justify-content:center;height:18px;background:var(--band)}
.days div{background:var(--band-light);height:19px;flex:1}
.days .wkend{background:var(--red)}
.dates div{background:var(--cell);color:var(--ink);height:23px;flex:1;font-size:9.5px;font-weight:600}
.dates .wkend{color:var(--red)}
.days{margin-top:5px}
</style>
</head>
<body>
<div class="page">
  <div class="hero" role="img" aria-label="Photo of an athlete stretching with a foam roller on a floodlit turf field at night"></div>
  <div class="challenge">Challenge<br>Of<br>The<br>Month</div>
  <div class="divider"></div>
  <p class="intro">Lorem ipsum dolor sit amet, consectetuer adipiscing elit, sed diam nonummy nibh euismod tincidunt ut laoreet dolore magna aliquam erat volutpat. Ut wisi enim ad minim veniam, quis nostrud exerci tation ullamcorper suscipit lobortis nisl ut aliquip ex ea commodo consequat. Duis autem vel eum iriure dolor in hendrerit in vulputate velit esse molestie consequat, vel illum dolore eu feugiat nulla facilisis at vero eros et accumsan et iusto odio dignissim qui blandit praesent luptatum zzril</p>
  <div class="month"><span>JANUARY</span></div>

  <div class="types"><div class="num">3</div><div class="label">Types Of Cardio</div></div>
  <div class="sidebar">
    <div class="cardio" style="top:22px"><h3>Running</h3><p>Lorem ipsum dolor sit amet, consectetuer adipiscing elit, sed diam nonummy nibh euismod tincidunt ut laoreet dolore magna aliquam erat volutpat. Ut</p></div>
    <div class="cardio" style="top:117px"><h3>Jumping</h3><p>Lorem ipsum dolor sit amet, consectetuer adipiscing elit, sed diam nonummy nibh euismod tincidunt ut laoreet dolore magna aliquam erat volutpat. Ut</p></div>
    <div class="cardio" style="top:212px"><h3>Cycling</h3><p>Lorem ipsum dolor sit amet, consectetuer adipiscing elit, sed diam nonummy nibh euismod tincidunt ut laoreet dolore magna aliquam erat volutpat. Ut</p></div>
  </div>
  <div class="column">
    <div class="note-line" style="top:125px"></div>
    <div class="note-line" style="top:249px"></div>
    <div class="note-line" style="top:373px"></div>
    <div class="note-line" style="top:497px"></div>
    <div class="note-line" style="top:621px"></div>
  </div>

  <div class="week" style="top:576px">
    <div class="tag"><div class="n">01</div><div class="w">WEEK</div></div>
    <div class="grid">
      <div class="row"><div style="width:187px">RUNNING</div><div style="flex:1">JUMPING</div></div>
      <div class="row"><div style="width:125px">CLIMBING</div><div style="width:187px">JUMPING</div><div style="flex:1">CYCLING</div></div>
      <div class="row days"><div>MON</div><div>TUE</div><div>WED</div><div>THU</div><div>FRI</div><div class="wkend">SAT</div><div class="wkend">SUN</div></div>
      <div class="row dates"><div>01</div><div>02</div><div>03</div><div>04</div><div>05</div><div class="wkend">06</div><div class="wkend">07</div></div>
    </div>
  </div>
  <div class="week" style="top:700px">
    <div class="tag"><div class="n">02</div><div class="w">WEEK</div></div>
    <div class="grid">
      <div class="row"><div style="width:187px">RUNNING</div><div style="flex:1">JUMPING</div></div>
      <div class="row"><div style="width:125px">CLIMBING</div><div style="width:187px">JUMPING</div><div style="flex:1">CYCLING</div></div>
      <div class="row days"><div>MON</div><div>TUE</div><div>WED</div><div>THU</div><div>FRI</div><div class="wkend">SAT</div><div class="wkend">SUN</div></div>
      <div class="row dates"><div>01</div><div>02</div><div>03</div><div>04</div><div>05</div><div class="wkend">06</div><div class="wkend">07</div></div>
    </div>
  </div>
  <div class="week" style="top:824px">
    <div class="tag"><div class="n">03</div><div class="w">WEEK</div></div>
    <div class="grid">
      <div class="row"><div style="width:187px">RUNNING</div><div style="flex:1">JUMPING</div></div>
      <div class="row"><div style="width:125px">CLIMBING</div><div style="width:187px">JUMPING</div><div style="flex:1">CYCLING</div></div>
      <div class="row days"><div>MON</div><div>TUE</div><div>WED</div><div>THU</div><div>FRI</div><div class="wkend">SAT</div><div class="wkend">SUN</div></div>
      <div class="row dates"><div>01</div><div>02</div><div>03</div><div>04</div><div>05</div><div class="wkend">06</div><div class="wkend">07</div></div>
    </div>
  </div>
  <div class="week" style="top:948px">
    <div class="tag"><div class="n">04</div><div class="w">WEEK</div></div>
    <div class="grid">
      <div class="row"><div style="width:187px">RUNNING</div><div style="flex:1">JUMPING</div></div>
      <div class="row"><div style="width:125px">CLIMBING</div><div style="width:187px">JUMPING</div><div style="flex:1">CYCLING</div></div>
      <div class="row days"><div>MON</div><div>TUE</div><div>WED</div><div>THU</div><div>FRI</div><div class="wkend">SAT</div><div class="wkend">SUN</div></div>
      <div class="row dates"><div>01</div><div>02</div><div>03</div><div>04</div><div>05</div><div class="wkend">06</div><div class="wkend">07</div></div>
    </div>
  </div>
  <div class="week" style="top:1073px">
    <div class="tag"><div class="n">05</div><div class="w">WEEK</div></div>
    <div class="grid">
      <div class="row"><div style="width:187px">RUNNING</div><div style="flex:1">JUMPING</div></div>
      <div class="row"><div style="width:125px">CLIMBING</div><div style="width:187px">JUMPING</div><div style="flex:1">CYCLING</div></div>
      <div class="row days"><div>MON</div><div>TUE</div><div>WED</div><div>THU</div><div>FRI</div><div class="wkend">SAT</div><div class="wkend">SUN</div></div>
      <div class="row dates"><div>01</div><div>02</div><div>03</div><div>04</div><div>05</div><div class="wkend">06</div><div class="wkend">07</div></div>
    </div>
  </div>
</div>
</body>
</html>
```